Packaging Design Project

Hello Designers,

Our company is a new start up looking to sell rice bagged in 50kg bags and sold to africa. This packaging should show that the product is trust worthy, homely and portray a mother love and trust ie your mother know the best food for her child.

Please find enclosed our company logo enclosed(Dunmoreton falls) and the name of the rice is sunny granary. We will add later sunny granary gold,premium and ultra .

Front Of the bag

Top of the bag is our logo

Name: Sunny Granary

Picture:to be done by you

Country of origin:Vietnam Parboiled RIce

Description:100% SORTEXED

Quality:premium quality

Back of bag

Name of company:DUNMORETON FALLS

Production Date:

expiry date:

Batch number:

Origination of product:PRODUCT OF VIETNAM

Exported by : name to be provided

Reason: I would like to see more designers. We were also asked for the length and breath of the 50kg bags. length is 92cm and breath is 63cm.

WE HAVE BEEN INFORMED BY THE BAG PRINTERS THAT WE ARE LIMITED TO ONLY 3 COLOURS.PLEASE CAN YOU UPDATE YOUR DESIGNS TO JUST 3 COLORS

Target Market(s)

The target market is all women above the age of 16.

Industry/Entity Type

It Company

Requirements
Must have
• We must have a picture of an african mother preferably smiling, her age must be at least 50 to 60 years of age.

```html
<!DOCTYPE html>
<html lang="en">
<head>
<meta charset="utf-8">
<title>Sunny Granary rice bag range</title>
<link rel="stylesheet" href="https://fonts.googleapis.com/css2?family=Bebas+Neue&family=Lora:wght@400&display=swap">
<style>
  :root {
    --page: #f2f2f2;
    --sack: #efede9;
    --sack-edge: #dcd9d3;
    --ink: #1d1d1d;
    --white: #ffffff;
    --mint: #80cfaf;
    --sun: #f8df70;
    --apricot: #f5a97c;
    --aqua: #92d8d3;
    --photo-light: #c9c9c9;
    --photo-dark: #4a4a4a;
  }
  * { box-sizing: border-box; margin: 0; padding: 0; }
  html, body { width: 858px; height: 1200px; overflow: hidden; background: var(--page); }
  .range { position: relative; width: 858px; height: 1200px; }
  .bag {
    position: absolute;
    width: 380px; height: 560px;
    background: var(--sack);
    border: 1px solid var(--sack-edge);
    border-radius: 10px 10px 4px 4px;
    overflow: hidden;
    --accent: var(--mint);
  }
  .bag--premium-mint { left: 34px; top: 22px; --accent: var(--mint); }
  .bag--premium-sun { left: 446px; top: 22px; --accent: var(--sun); }
  .bag--golden { left: 34px; top: 620px; --accent: var(--apricot); }
  .bag--ultra { left: 446px; top: 620px; --accent: var(--aqua); }

  .band {
    position: absolute;
    left: 118px; top: 0;
    width: 138px; height: 100%;
    background: var(--accent);
  }
  .maker {
    position: absolute;
    top: 24px; left: 0; width: 100%;
    display: flex; align-items: center; justify-content: center; gap: 4px;
    font-family: "Bebas Neue", sans-serif;
    font-size: 11px; line-height: 12px; letter-spacing: 0.5px;
    color: var(--ink);
  }
  .maker__dot { width: 7px; height: 7px; border-radius: 50%; background: var(--ink); }
  .seal {
    position: absolute;
    left: 26px; top: 48px;
    width: 86px; height: 86px;
    border-radius: 50%;
    background: var(--white);
    display: flex; align-items: center; justify-content: center;
    font-family: "Bebas Neue", sans-serif;
    font-size: 14px; letter-spacing: 0.2px;
    color: var(--accent);
    text-align: center; line-height: 1;
    white-space: nowrap;
  }
  .descriptor {
    position: absolute;
    left: 12px; top: 150px; width: 114px;
    text-align: center;
    font-family: "Bebas Neue", sans-serif;
    font-size: 17px; line-height: 1;
    color: var(--ink);
  }
  .descriptor span { display: block; padding: 1px 0; }
  .descriptor span:last-child { border-bottom: 1px solid var(--ink); padding-bottom: 3px; }
  .grade {
    position: absolute;
    left: 43px; top: 238px;
    width: 52px; height: 52px;
    border-radius: 50%;
    border: 1.5px solid var(--white);
    display: flex; align-items: center; justify-content: center;
    text-align: center;
    font-family: "Lora", serif;
    font-size: 9px; line-height: 1.15;
    color: var(--white);
  }
  .portrait {
    position: absolute;
    left: 86px; top: 318px;
    width: 208px; height: 242px;
    border-radius: 100px 100px 0 0;
    background: linear-gradient(180deg, var(--photo-light) 0%, #8e8e8e 55%, var(--photo-dark) 100%);
  }
  .weight {
    position: absolute;
    left: 170px; top: 518px;
    width: 36px; height: 36px;
    border-radius: 50%;
    background: var(--accent);
    display: flex; align-items: center; justify-content: center;
    font-family: "Lora", serif;
    font-size: 10px;
    color: var(--white);
  }
</style>
</head>
<body>
<main class="range">

  <section class="bag bag--premium-mint">
    <div class="band">
      <div class="maker"><span class="maker__dot"></span>DUNMORETON FALLS</div>
      <div class="seal">SUNNY GRANARY</div>
      <div class="descriptor"><span>100% SORTEXED</span><span>VIETNAM</span><span>PARBOILED RICE</span></div>
      <div class="grade">Premium<br>quality</div>
    </div>
    <div class="portrait" role="img" aria-label="Black and white portrait photograph of a smiling mother"></div>
    <div class="weight">50 kg</div>
  </section>

  <section class="bag bag--premium-sun">
    <div class="band">
      <div class="maker"><span class="maker__dot"></span>DUNMORETON FALLS</div>
      <div class="seal">SUNNY GRANARY</div>
      <div class="descriptor"><span>100% SORTEXED</span><span>VIETNAM</span><span>PARBOILED RICE</span></div>
      <div class="grade">Premium<br>quality</div>
    </div>
    <div class="portrait" role="img" aria-label="Black and white portrait photograph of a smiling mother"></div>
    <div class="weight">50 kg</div>
  </section>

  <section class="bag bag--golden">
    <div class="band">
      <div class="maker"><span class="maker__dot"></span>DUNMORETON FALLS</div>
      <div class="seal">SUNNY GRANARY</div>
      <div class="descriptor"><span>100% SORTEXED</span><span>VIETNAM</span><span>PARBOILED RICE</span></div>
      <div class="grade">Golden<br>quality</div>
    </div>
    <div class="portrait" role="img" aria-label="Black and white portrait photograph of a smiling mother"></div>
    <div class="weight">50 kg</div>
  </section>

  <section class="bag bag--ultra">
    <div class="band">
      <div class="maker"><span class="maker__dot"></span>DUNMORETON FALLS</div>
      <div class="seal">SUNNY GRANARY</div>
      <div class="descriptor"><span>100% SORTEXED</span><span>VIETNAM</span><span>PARBOILED RICE</span></div>
      <div class="grade">Ultra<br>quality</div>
    </div>
    <div class="portrait" role="img" aria-label="Black and white portrait photograph of a smiling mother"></div>
    <div class="weight">50 kg</div>
  </section>

</main>
</body>
</html>
```